Olive oil bottle labels, front and back.

Sophisticated uncluttered distinctive eye catching label
Front label:
Label on front like the uploaded file in design but called “Tallow Brook”, (not Marrowind Bay.)
Need to state that it’s extra virgin, cold pressed olive oil, 100% organic, grown and pressed on the Mornington Peninsula.
500 ml
Back label:
Nutritional information table (see label example in uploaded files) including FFA 0.1% Oleic Acid
Storage: airtight in cool dark place
Made and produced in Australia from 100% Australian ingredients,
Harvest date:
Best by:
Batch:
Grown, harvested and bottled at The Hollow, Pettisby Rd. Carrowmere. 3814
The back label on uploaded files has the info requited except they should have address and don't include those industry and Australian made logos.
The front label is what we want, first to plagiarise without copyright infringement gets the gig, thanks.
Labels front and back need be 5 x 13 cm
Gourmet, up-market
- Love "Adorn Regular Garland"

```html
<!DOCTYPE html>
<html lang="en">
<head>
<meta charset="utf-8">
<title>Tallow Brook Olive Oil Labels</title>
<link rel="stylesheet" href="https://fonts.googleapis.com/css2?family=Allura&family=Fira+Sans:wght@300;400;600&family=Libre+Caslon+Text&display=swap">
<style>
  :root {
    --backdrop: #7f7b79;
    --label-black: #141414;
    --gold: #b8973f;
    --gold-light: #c9ab5c;
    --white: #f4f2ee;
    --rule: #cfcac2;
    --badge-green: #7fb63a;
  }
  * { box-sizing: border-box; margin: 0; padding: 0; }
  html, body { width: 1197px; height: 1200px; overflow: hidden; }
  body {
    background: var(--backdrop);
    position: relative;
    font-family: "Fira Sans", sans-serif;
    color: var(--white);
  }
  .label {
    position: absolute;
    top: 157px;
    width: 356px;
    height: 925px;
    background: var(--label-black);
    overflow: hidden;
  }
  .label--front { left: 140px; }
  .label--back { left: 702px; }

  /* Front */
  .gold-band {
    position: absolute; inset: 0;
    background: linear-gradient(90deg, #a98a42 0%, #b69748 18%, #8a7034 26%, #3a2f18 30%, var(--label-black) 33%);
  }
  .front-wordmark {
    position: absolute;
    left: 12px; bottom: 20px;
    transform-origin: left bottom;
    transform: rotate(-90deg) translateY(100%);
    font-family: "Allura", cursive;
    font-size: 150px;
    line-height: 1;
    white-space: nowrap;
    color: var(--white);
    width: 900px;
  }
  .olive-photo {
    position: absolute;
    left: 158px; top: 247px;
    width: 186px; height: 100px;
    background: radial-gradient(ellipse at 45% 55%, #d98f1c 0%, #b8741a 28%, #3d4a2c 55%, rgba(20,20,20,0) 75%);
  }
  .front-copy {
    position: absolute;
    right: 40px;
    text-align: right;
  }
  .style-line {
    top: 378px;
    font-weight: 600;
    font-size: 14px;
    letter-spacing: 1.6px;
    line-height: 20px;
  }
  .product-name {
    top: 426px;
    font-family: "Libre Caslon Text", serif;
    font-size: 40px;
    line-height: 44px;
    color: var(--gold);
  }
  .organic-badge {
    position: absolute;
    left: 259px; top: 654px;
  }
  .origin-line {
    top: 728px;
    font-size: 16px;
    line-height: 21px;
  }
  .volume {
    top: 802px;
    font-size: 26px;
    font-weight: 300;
    color: var(--gold);
  }

  /* Back */
  .back-wordmark {
    position: absolute;
    top: 66px; left: 0; right: 0;
    text-align: center;
    font-family: "Allura", cursive;
    font-size: 24px;
    color: var(--gold);
    padding-left: 4px;
  }
  .back-heading {
    position: absolute;
    left: 0; right: 0;
    text-align: center;
    font-size: 17.5px;
    letter-spacing: 0.4px;
  }
  .nutrition-title { top: 118px; }
  .nutrition {
    position: absolute;
    left: 42px; width: 268px; top: 155px;
    font-size: 13.5px;
    font-weight: 300;
  }
  .nutrition table { width: 100%; border-collapse: collapse; border-top: 1.5px solid var(--rule); border-bottom: 1.5px solid var(--rule); }
  .nutrition td { line-height: 19.8px; padding: 0 4px; white-space: nowrap; }
  .nutrition td.num { text-align: right; width: 52px; }
  .nutrition thead td { padding-top: 6px; padding-bottom: 2px; vertical-align: top; line-height: 19px; }
  .nutrition thead tr { border-bottom: 1.5px solid var(--rule); }
  .nutrition tbody tr:first-child td { padding-top: 4px; }
  .nutrition tbody tr:last-child td { padding-bottom: 4px; }
  .nutrition .sub { padding-left: 9px; }
  .ingredients-title { top: 462px; }
  .back-text {
    position: absolute;
    left: 30px; right: 30px;
    text-align: center;
    font-size: 14.5px;
    font-weight: 300;
    line-height: 20px;
  }
  .ingredients { top: 486px; }
  .storage { top: 532px; color: var(--gold); font-weight: 400; font-size: 14px; }
  .rule {
    position: absolute;
    left: 42px; width: 268px;
    border-top: 1.5px solid var(--rule);
  }
  .rule--a { top: 557px; }
  .rule--b { top: 612px; }
  .made-in { top: 566px; }
  .grown-at { top: 620px; }
  .date-panel {
    position: absolute;
    left: 64px; top: 812px;
    width: 228px; height: 82px;
    background: #fff;
    color: #111;
    padding: 4px 10px;
    font-size: 14px;
    line-height: 24px;
    font-weight: 400;
  }
</style>
</head>
<body>

<section class="label label--front">
  <div class="gold-band"></div>
  <div class="front-wordmark">Tallow Brook</div>
  <div class="olive-photo" role="img" aria-label="Photograph of two ripe olives with leaves"></div>
  <p class="front-copy style-line">EXTRA VIRGIN<br>COLD PRESSED</p>
  <p class="front-copy product-name">OLIVE<br>OIL</p>
  <svg class="organic-badge" width="56" height="56" viewBox="0 0 56 56" aria-hidden="true">
    <circle cx="28" cy="28" r="25" fill="none" stroke="var(--badge-green)" stroke-width="1.6"/>
  </svg>
  <p class="front-copy origin-line">Grown and pressed<br>on the Mornington<br>Peninsula</p>
  <p class="front-copy volume">500ml</p>
</section>

<section class="label label--back">
  <div class="back-wordmark">Tallow Brook</div>
  <h2 class="back-heading nutrition-title">NUTRITION INFORMATION</h2>
  <div class="nutrition">
    <table>
      <thead>
        <tr><td>AVG QTY</td><td class="num">PER<br>15ml</td><td class="num">PER<br>100ml</td></tr>
      </thead>
      <tbody>
        <tr><td>ENERGY (KJ)</td><td class="num">517</td><td class="num">3446</td></tr>
        <tr><td>PROTEIN (G)</td><td class="num">0</td><td class="num">0</td></tr>
        <tr><td>FAT</td><td class="num"></td><td class="num"></td></tr>
        <tr><td class="sub">- Total</td><td class="num">13.7</td><td class="num">91.5</td></tr>
        <tr><td class="sub">- Saturated</td><td class="num">2.1</td><td class="num">14.1</td></tr>
        <tr><td class="sub">- Monounsaturated</td><td class="num">10.7</td><td class="num">71.5</td></tr>
        <tr><td class="sub">- Polyunsaturated</td><td class="num">0.9</td><td class="num">5.9</td></tr>
        <tr><td class="sub">- Trans Fatty Acid</td><td class="num">&lt;0.01</td><td class="num">&lt;0.05</td></tr>
        <tr><td class="sub">- FFA (Oleic Acid)</td><td class="num">0.1</td><td class="num">0.5</td></tr>
        <tr><td>CHOLESTEROL (MG)</td><td class="num">0</td><td class="num">0</td></tr>
        <tr><td>CARBONHYDRATE (G)</td><td class="num">0</td><td class="num">0</td></tr>
        <tr><td class="sub">- Sugar (G)</td><td class="num">0</td><td class="num">0</td></tr>
      </tbody>
    </table>
  </div>
  <h2 class="back-heading ingredients-title">INGREDIENTS</h2>
  <p class="back-text ingredients">100% Australian Extra virgin olive oil<br>(Cold pressed fresh)</p>
  <p class="back-text storage">STORE AIRTIGHT IN A COOL DARK PLACE</p>
  <div class="rule rule--a"></div>
  <p class="back-text made-in">Made in Australia from 100%<br>Australian ingredients</p>
  <div class="rule rule--b"></div>
  <p class="back-text grown-at">Grown, harvest and bottled at the<br>Hollow, Pettisby Rd. Carrowmere. 3814</p>
  <div class="date-panel">Harvest date:<br>Best by:<br>Batch:</div>
</section>

</body>
</html>
```